Luxury Brand Real Estate For Sale sign

**Update** I've added some examples from the internet of other signs that have a look similar to what I would like to see. I do not want my personal name in the sign. And the word FOR SALE Does not need to be so large - it can be more subtle.
I want to create a Real Estate for sale sign for my company that will be used for luxury/higher end real estate listings. I’m sharing my business card as well as a logo with new teal color to show what we're moving towards: we’re using Teal, white, black and gold.
Hoping the sign is simple, sophisticated and eye catching.
The sign should be 24" wide by 30" tall including the company name: Harbor Crest Realty Group and our logo, office phone number 727-555-0148 and website www.hcrgproperty.example the words "For Sale"
Optional to add this e-mail address info@hcrgproperty.example to the sign
Luxury home buyers
Real Estate

```html
<!DOCTYPE html>
<html lang="en">
<head>
<meta charset="utf-8">
<title>Harbor Crest Realty Group – For Sale Sign</title>
<link rel="stylesheet" href="https://fonts.googleapis.com/css2?family=Montserrat:wght@300;400;500;600&display=swap">
<style>
  :root {
    --page: #ffffff;
    --teal: #4f7363;
    --gold: #e2a729;
    --white: #ffffff;
  }
  * { margin: 0; padding: 0; box-sizing: border-box; }
  html, body { width: 943px; height: 1200px; overflow: hidden; background: var(--page); }
  .canvas { position: relative; width: 943px; height: 1200px; font-family: 'Montserrat', sans-serif; }

  .sign {
    position: absolute; left: 187px; top: 244px; width: 571px; height: 711px;
    background: var(--teal);
  }
  .sign-frame {
    position: absolute; left: 26px; top: 27px; width: 517px; height: 658px;
    border: 2px solid var(--gold);
  }
  .frame-accent {
    position: absolute; left: 348px; top: 629px; width: 195px; height: 2px;
    background: var(--gold);
  }

  .brand-mark {
    position: absolute; left: 53px; top: 142px;
    font-size: 40px; font-weight: 500; color: var(--gold); letter-spacing: 0.01em;
  }
  .brand-divider {
    position: absolute; left: 194px; top: 72px; width: 2px; height: 157px;
    background: var(--white);
  }
  .brand-name { position: absolute; left: 217px; top: 128px; }
  .brand-name-primary {
    display: block; font-size: 29px; font-weight: 500; color: var(--gold);
    line-height: 1; letter-spacing: -0.01em;
  }
  .brand-name-secondary {
    display: block; margin-top: 8px; font-size: 15px; font-weight: 600; color: var(--white);
    line-height: 1; letter-spacing: 0.32em;
  }

  .listing-status {
    position: absolute; left: 0; width: 100%; top: 342px; text-align: center;
    font-size: 84px; font-weight: 300; color: var(--gold); line-height: 1; letter-spacing: 0.02em;
  }
  .office-phone {
    position: absolute; left: 0; width: 100%; top: 526px; text-align: center;
    font-size: 48px; font-weight: 500; color: var(--white); line-height: 1;
  }
  .contact-lines {
    position: absolute; left: 53px; top: 605px; width: 280px;
    font-size: 19px; font-weight: 400; color: var(--white); line-height: 30px;
    white-space: nowrap;
  }
</style>
</head>
<body>
<div class="canvas">
  <section class="sign" aria-label="Harbor Crest Realty Group for sale sign">
    <div class="sign-frame"></div>
    <div class="frame-accent"></div>

    <div class="brand-mark">HCRG</div>
    <div class="brand-divider"></div>
    <div class="brand-name">
      <span class="brand-name-primary">HARBOR CREST</span>
      <span class="brand-name-secondary">REALTY GROUP</span>
    </div>

    <h1 class="listing-status">FOR SALE</h1>

    <p class="office-phone">727-555-0148</p>

    <div class="contact-lines">
      <p class="contact-email">info@hcrgproperty.example</p>
      <p class="contact-web">www.hcrgproperty.example</p>
    </div>
  </section>
</div>
</body>
</html>
```